A Volume Worth Trading - book cover (front panel only)

I want a book cover (for print and ebook) in a distinctive, quirky style that can be repurposed for podcast artwork too. Full brief supplied.
The book is a practical, accessible handbook for anyone thinking about writing a book to build their business, with a wide range of tips and techniques to help plan, write, publishing and promote a book that’s integrated with your platform and works to build your reputation, network and credibility from day 1.
The target audience is experts in business, particularly owners of SMEs with an established online and offline platform (eg speaking, training, consulting) who want to add a book to take their business to the next level.
I want the design to be strong and distinctive, slightly quirky without being gimmicky, with the focus on typography.

Target Market(s)

Those writing a book based on their expertise to build their business

Industry/Entity Type

Publishing Company

Font styles to use
Serif
Sans Serif
Decorative

Colors

Designer to choose colors to be used in the design.

Requirements
Must have
• Commercially appealing book cover design, with application files and copyright supplied, front panel only, 5.5 x 8.5 inch format. Must work at both full size and thumbnail.
Nice to have
• A distinctive style that could be applied across other products in my portfolio.

```html
<!DOCTYPE html>
<html lang="en">
<head>
<meta charset="utf-8">
<title>A Volume Worth Trading – Cover</title>
<link rel="stylesheet" href="https://fonts.googleapis.com/css2?family=Bodoni+Moda:opsz,wght@6..96,700&family=Questrial&display=swap">
<style>
  :root {
    --backdrop: #786e6b;
    --paper: #ffffff;
    --title-green: #2e6427;
    --title-red: #8b2e1e;
    --art-mustard: #e6b945;
    --art-lime: #afc03c;
    --frame: #222222;
  }
  html, body {
    margin: 0;
    width: 1200px;
    height: 1200px;
    overflow: hidden;
    background: var(--backdrop);
  }
  .cover {
    position: absolute;
    left: 418px;
    top: 321px;
    width: 340px;
    height: 525px;
    background: var(--paper);
    outline: 1.5px solid var(--frame);
    overflow: hidden;
  }
  .cover-title {
    position: absolute;
    left: 0;
    top: 0;
    width: 340px;
    height: 178px;
  }
  .cover-title text {
    font-family: "Bodoni Moda", "Didot", serif;
    font-weight: 700;
  }
  .title-top { fill: var(--title-green); }
  .title-main { fill: var(--title-red); }
  .subtitle-band {
    position: absolute;
    left: 0;
    top: 178px;
    width: 340px;
    height: 34px;
    background: var(--title-red);
    color: var(--paper);
    font-family: "Questrial", sans-serif;
    font-size: 10.5px;
    line-height: 13px;
    letter-spacing: 1.05px;
    text-transform: uppercase;
    box-sizing: border-box;
    padding: 4px 0 0 22px;
  }
  .author {
    position: absolute;
    left: 0;
    top: 216px;
    width: 340px;
    text-align: center;
    color: var(--title-red);
    font-family: "Questrial", sans-serif;
    font-size: 16px;
    letter-spacing: 1.6px;
    text-transform: uppercase;
  }
  .cover-art {
    position: absolute;
    left: 57px;
    top: 237px;
    width: 232px;
    height: 270px;
    background: linear-gradient(135deg, var(--art-lime) 0%, var(--art-mustard) 45%, var(--art-mustard) 70%, var(--title-red) 100%);
  }
</style>
</head>
<body>
  <main class="cover">
    <svg class="cover-title" viewBox="0 0 340 178" aria-label="A Volume Worth Trading">
      <text class="title-top" x="25" y="75" font-size="76" textLength="291" lengthAdjust="spacingAndGlyphs">A VOLUME WORTH</text>
      <text class="title-main" x="27" y="175" font-size="138" textLength="289" lengthAdjust="spacingAndGlyphs">TRADING</text>
    </svg>
    <div class="subtitle-band">Clever ways to plan and write a book<br>that works harder for your business</div>
    <div class="author">Helen Marsh</div>
    <div class="cover-art" role="img" aria-label="Illustration of a mustard notebook with a red pen lying across it, surrounded by green business icons: dollar signs, percent, chart, clock and document"></div>
  </main>
</body>
</html>
```